Business card design for online Mandarin Learning School

We need a business card design for our online language learning school called "Maple Bridge Online for Mandarin Learning". Our existing website is https://www.maplebridgeonline.com
We have our logo already. We would like to see our business card design that can make our online teaching services to be innovative, young, energetic and fun to learn. Prefer to have a certain level of color matching with our website. Apart from "Maple Bridge Online", need to specifically state "for Mandarin Learning" as well on the business card.

```html
<!DOCTYPE html>
<html lang="en">
<head>
<meta charset="utf-8">
<title>Maple Bridge Online – Business Card</title>
<link rel="stylesheet" href="https://fonts.googleapis.com/css2?family=Cinzel:wght@400;700&family=Crimson+Text:wght@400&display=swap">
<style>
  :root {
    --teal: #12a9b6;
    --teal-deep: #0f96a2;
    --coral: #e0585a;
    --grey: #8a8a8a;
    --white: #ffffff;
    --backdrop: #ece9e4;
    --shadow: rgba(0, 0, 0, 0.18);
  }
  * { margin: 0; padding: 0; box-sizing: border-box; }
  html, body { width: 1200px; height: 1040px; overflow: hidden; }
  body {
    background: var(--backdrop);
    position: relative;
    font-family: "Crimson Text", Georgia, serif;
  }
  .card {
    position: absolute;
    border-radius: 26px;
    box-shadow: 0 10px 30px var(--shadow);
    overflow: hidden;
  }
  /* Front */
  .card-front {
    left: 70px; top: 250px;
    width: 580px; height: 340px;
    background: var(--white);
    display: flex; align-items: center; justify-content: center;
    gap: 22px;
  }
  .brand-dot {
    width: 34px; height: 34px; border-radius: 50%;
    background: var(--teal);
  }
  .brand-name {
    font-family: "Cinzel", "Times New Roman", serif;
    font-weight: 400;
    font-size: 52px;
    letter-spacing: 3px;
    color: var(--teal);
  }
  /* Back */
  .card-back {
    left: 760px; top: 120px;
    width: 340px; height: 580px;
    background: var(--teal);
    color: var(--white);
    text-align: center;
    padding-top: 52px;
  }
  .holder-name {
    font-family: "Cinzel", "Times New Roman", serif;
    font-weight: 700;
    font-size: 25px;
    letter-spacing: 1px;
  }
  .holder-role {
    font-family: "Cinzel", "Times New Roman", serif;
    font-size: 15px;
    letter-spacing: 1px;
    margin-top: 2px;
  }
  .address, .contacts {
    font-size: 16px;
    line-height: 1.25;
    letter-spacing: 0.5px;
  }
  .address { margin-top: 22px; }
  .contacts { margin-top: 20px; }
  .social-row {
    display: flex; justify-content: center; gap: 6px;
    margin-top: 20px;
  }
  .social-dot {
    width: 22px; height: 22px; border-radius: 50%;
    border: 1.5px solid var(--white);
  }
  .back-brand {
    position: absolute; left: 0; right: 0; bottom: 44px;
    text-align: center;
  }
  .back-brand-name {
    font-family: "Cinzel", "Times New Roman", serif;
    font-weight: 400;
    font-size: 30px;
    letter-spacing: 2px;
    color: var(--white);
  }
  .back-brand-tag {
    font-size: 17px;
    color: var(--white);
    margin-top: 4px;
    letter-spacing: 0.5px;
  }
</style>
</head>
<body>
  <section class="card card-front" aria-label="Card front">
    <span class="brand-dot"></span>
    <span class="brand-name">MAPLE BRIDGE</span>
  </section>

  <section class="card card-back" aria-label="Card back">
    <h1 class="holder-name">DANIEL REYES</h1>
    <p class="holder-role">CEO/FOUNDER</p>
    <p class="address">2140 Willow Crest Road<br>Juneau, Alaska 34812</p>
    <p class="contacts">
      Tel: 555 214 7730<br>
      Cel: 555 389 4126<br>
      Fax: 555 602 1858<br>
      info@maplebridgeonline.com<br>
      www.maplebridgeonline.com
    </p>
    <div class="social-row" aria-label="Social links">
      <span class="social-dot"></span>
      <span class="social-dot"></span>
      <span class="social-dot"></span>
    </div>
    <div class="back-brand">
      <p class="back-brand-name">MAPLE BRIDGE</p>
      <p class="back-brand-tag">Online for Mandarin Learning</p>
    </div>
  </section>
</body>
</html>
```